Gift voucher for a photo shoot, folding card DIN long (21 x 9.8 cm)

Hello, I'm a professional photographer and need a new design for my gift voucher card for a photo shoot. The design should be applicable to all types of photo shoots (neutral). I prefer a sophisticated design. The folded card should be printed on both sides.
My data should be included: Logo, Address: Wendtaler Gasse 9, 07318 Gera, Email: fotograf@jonasbirkner.eu, Website: www.jonasbirkner.eu Tel.: 0176 / 4389025
Updates

Please design the folding card in DIN long format (105 x 210 mm, landscape format). The card should open horizontally. Please design the front with the words "Gift voucher for you" and my logo. Please make the logo small – the words "Gift voucher" should be in the foreground.
The colors - use elegant gray with gold or white font color.
The inside should contain the words: Photo shoot for ........ worth .....€, as well as my logo.
My contact details should be on the back.

Target Market(s)

Private customer

Colors

Designer to choose only greyscale colors for use in the design.

Requirements
Must have
• Noble appearance, a gift voucher that one likes to give away, words: Gift voucher for you, photo shoot for ..., worth .......€
Nice to have
• Noble appearance of the gift voucher, a gift voucher that you like to give away
Should not have
• no pictures

```html
<!DOCTYPE html>
<html lang="de">
<head>
<meta charset="utf-8">
<title>Gift Voucher – Jonas Birkner</title>
<link href="https://fonts.googleapis.com/css2?family=Montserrat:wght@400;500;700&family=Pinyon+Script&family=Tenor+Sans&display=swap" rel="stylesheet">
<style>
  :root {
    --stage: #000000;
    --card-grey: #474849;
    --paper: #f6f6f7;
    --white: #ffffff;
    --ink: #3a3b3d;
    --gold-dark: #b07d12;
    --gold: #e0ad2c;
    --gold-light: #f6dc8c;
  }
  * { margin: 0; padding: 0; box-sizing: border-box; }
  html, body { width: 1200px; height: 994px; overflow: hidden; background: var(--stage); }
  .canvas {
    width: 1200px; height: 994px;
    display: flex; flex-direction: column; align-items: center; justify-content: center;
    gap: 32px;
  }
  .panel { width: 600px; height: 300px; position: relative; overflow: hidden; }

  /* Front */
  .front { background: var(--card-grey); }
  .brand-mark {
    position: absolute; left: 38px; top: 108px; width: 120px;
    display: flex; flex-direction: column; align-items: center; gap: 10px;
  }
  .brand-dot { width: 46px; height: 46px; border: 2px solid var(--white); border-radius: 50%; }
  .brand-name {
    font-family: "Montserrat", sans-serif; font-weight: 500; font-size: 13px;
    color: var(--white); letter-spacing: 1px; white-space: nowrap;
  }
  .divider { position: absolute; left: 195px; top: 76px; width: 1px; height: 147px; background: #8a8b8c; }
  .gift-word {
    position: absolute; left: 190px; top: 39px;
    display: inline-block;
    padding: 20px 70px 45px 30px;
    font-family: "Pinyon Script", cursive; font-size: 145px; line-height: 1;
    white-space: nowrap;
    background: linear-gradient(100deg, var(--gold-dark) 15%, var(--gold-light) 45%, var(--gold) 65%, var(--gold-dark) 85%);
    -webkit-background-clip: text; background-clip: text; color: transparent;
  }
  .voucher-line {
    position: absolute; left: 350px; top: 174px; z-index: 1;
    font-family: "Tenor Sans", sans-serif; font-size: 27px; color: var(--gold);
    white-space: nowrap;
  }

  /* Inside */
  .inside { background: var(--paper); }
  .inside-head {
    height: 150px; background: var(--card-grey);
    display: flex; flex-direction: column; align-items: center; justify-content: center; gap: 12px;
  }
  .inside-head .brand-dot { width: 56px; height: 56px; }
  .inside-head .brand-name { font-size: 26px; letter-spacing: 2px; }
  .gold-band {
    height: 6px;
    background: linear-gradient(90deg, var(--gold-dark), var(--gold) 30%, var(--gold-light) 55%, var(--gold) 75%, var(--gold-dark));
  }
  .fill-in {
    position: absolute; left: 49px; top: 210px;
    font-family: "Montserrat", sans-serif; font-size: 28px; color: var(--ink);
    display: flex; align-items: baseline; white-space: nowrap;
  }
  .blank { display: inline-block; border-bottom: 1px solid var(--ink); height: 1px; }
  .blank-short { width: 88px; }
  .blank-long { width: 92px; }

  /* Back */
  .back {
    background: var(--card-grey);
    display: flex; flex-direction: column; align-items: center; justify-content: flex-end;
    padding-bottom: 38px;
    font-family: "Montserrat", sans-serif; font-size: 18px; color: var(--white);
    letter-spacing: 1.6px; line-height: 33px; text-align: center;
  }
  .back .phone { font-weight: 700; letter-spacing: 1px; }
</style>
</head>
<body>
<main class="canvas">
  <section class="panel front" aria-label="Front">
    <div class="brand-mark">
      <span class="brand-dot"></span>
      <span class="brand-name">Jonas Birkner</span>
    </div>
    <span class="divider"></span>
    <span class="gift-word">gift</span>
    <span class="voucher-line">Voucher for you</span>
  </section>

  <section class="panel inside" aria-label="Inside">
    <div class="inside-head">
      <span class="brand-dot"></span>
      <span class="brand-name">Jonas Birkner</span>
    </div>
    <div class="gold-band"></div>
    <p class="fill-in">Photo shoot for<span class="blank blank-short"></span>worth<span class="blank blank-long"></span>€</p>
  </section>

  <section class="panel back" aria-label="Back">
    <p>Wendtaler Gasse 9, 07318 Gera,</p>
    <p>fotograf@jonasbirkner.eu</p>
    <p>www.jonasbirkner.eu</p>
    <p class="phone">0176 / 4389025</p>
  </section>
</main>
</body>
</html>
```